New Company Business Card Design

I have a new company logo and I want a new business card design. I dont know if the logo file i attached is in the correct format or quality. We are a New York City Specialty construction Firm specializing in high risk out of the box projects. I want a simple and classy business card that people will his card is as crisp as the work his company does.

Target Market(s)

Clients in the heavy construction industry in New York City

Industry/Entity Type

Construction Company

Contact Information for Business Card

Simple Classy - DIFFERENT

Font styles to use
Other font styles liked:
• Mach the logo font in some way

Colors

Designer to choose colors to be used in the design.

Requirements
Must have
• Uniqueness
Nice to have
• Nothing particular - Just different and classy - Timeless
Should not have
• Goofy Shit or Gimmicky shit

```html
<!DOCTYPE html>
<html lang="en">
<head>
<meta charset="utf-8">
<title>Ardent Rigging Co. — Business Card</title>
<link href="https://fonts.googleapis.com/css2?family=Roboto:wght@400;500;700;900&family=Montserrat:wght@500&display=swap" rel="stylesheet">
<style>
  :root {
    --backdrop: #3a3a3a;
    --card-dark: #1c1c1d;
    --card-light: #ffffff;
    --brand-blue: #1e73be;
    --brand-blue-light: #3a9ad9;
    --ink: #3c3c3c;
    --ink-soft: #5a5a5a;
    --rule: #9a9a9a;
    --band: #121212;
  }
  * { margin: 0; padding: 0; box-sizing: border-box; }
  html, body { width: 1200px; height: 900px; overflow: hidden; }
  body {
    background: var(--backdrop);
    font-family: "Roboto", Arial, sans-serif;
    position: relative;
  }
  .card {
    position: absolute;
    left: 320px;
    width: 560px;
    height: 320px;
    box-shadow: 0 10px 30px rgba(0,0,0,.45);
    overflow: hidden;
  }
  /* Front */
  .card-front { top: 80px; background: var(--card-dark); }
  .card-front .wordmark {
    position: absolute; left: 0; right: 0; top: 112px;
    text-align: center;
    font-weight: 900; font-size: 40px; letter-spacing: 2px;
    color: var(--brand-blue-light);
  }
  .wordmark .mark-square {
    display: inline-block; width: 22px; height: 22px;
    background: var(--brand-blue-light);
    margin-right: 12px; vertical-align: 2px;
  }
  .card-front .web {
    position: absolute; left: 0; right: 0; top: 248px;
    text-align: center;
    font-family: "Montserrat", Arial, sans-serif;
    font-size: 14px; letter-spacing: 3px; color: #d8d8d8;
  }
  /* Back */
  .card-back { top: 470px; background: var(--card-light); }
  .card-back .wordmark {
    position: absolute; left: 30px; top: 52px;
    font-weight: 900; font-size: 26px; letter-spacing: 1px;
    color: var(--brand-blue);
  }
  .card-back .wordmark .mark-square {
    width: 16px; height: 16px; margin-right: 9px; background: var(--brand-blue);
  }
  .identity {
    position: absolute; right: 34px; top: 50px; text-align: right;
  }
  .identity .person { font-weight: 700; font-size: 24px; color: var(--brand-blue); }
  .identity .role { font-size: 18px; color: var(--ink-soft); margin-top: 2px; }
  .rule-top {
    position: absolute; left: 30px; right: 34px; top: 118px;
    height: 1px; background: var(--rule);
  }
  .address {
    position: absolute; right: 34px; top: 150px;
    text-align: right; font-size: 14px; line-height: 20px; color: var(--ink-soft);
  }
  .rule-contact {
    position: absolute; left: 30px; width: 200px; top: 196px;
    height: 1px; background: var(--rule);
  }
  .contacts {
    position: absolute; left: 30px; top: 204px;
    list-style: none; font-size: 14px; color: var(--ink);
  }
  .contacts li { display: flex; align-items: center; height: 21px; }
  .contacts svg { width: 13px; height: 13px; margin-right: 8px; fill: var(--brand-blue); }
  .footer-band { position: absolute; left: 0; bottom: 0; width: 560px; height: 90px; }
  .footer-web {
    position: absolute; right: 26px; top: 281px;
    font-size: 13px; line-height: 16px; letter-spacing: 1px; color: #ffffff;
  }
</style>
</head>
<body>

<section class="card card-front">
  <div class="wordmark"><span class="mark-square"></span>ARDENT RIGGING</div>
  <div class="web">ARDENTRIG.COM</div>
</section>

<section class="card card-back">
  <div class="wordmark"><span class="mark-square"></span>ARDENT RIGGING</div>

  <div class="identity">
    <div class="person">Marcus T. Rennick</div>
    <div class="role">President</div>
  </div>
  <div class="rule-top"></div>

  <div class="address">118 Harbor Yard Road<br>Linden, New Jersey 07036</div>

  <div class="rule-contact"></div>
  <ul class="contacts">
    <li><svg viewBox="0 0 24 24"><path d="M6.6 10.8a15 15 0 0 0 6.6 6.6l2.2-2.2c.3-.3.7-.4 1-.2 1.1.4 2.3.6 3.6.6.6 0 1 .4 1 1V20c0 .6-.4 1-1 1A17 17 0 0 1 3 4c0-.6.4-1 1-1h3.5c.6 0 1 .4 1 1 0 1.3.2 2.5.6 3.6.1.3 0 .7-.2 1z"/></svg>908-555-0142</li>
    <li><svg viewBox="0 0 24 24"><path d="M7 1h10a2 2 0 0 1 2 2v18a2 2 0 0 1-2 2H7a2 2 0 0 1-2-2V3a2 2 0 0 1 2-2zm0 3v15h10V4z"/></svg>917-555-0187</li>
    <li><svg viewBox="0 0 24 24"><path d="M2 5h20v14H2zm2 2v.5l8 5 8-5V7l-8 5z"/></svg>MARCUS@ARDENTRIG.COM</li>
  </ul>

  <svg class="footer-band" viewBox="0 230 560 90" aria-hidden="true">
    <path d="M330 320 Q372 302 392 282 Q406 270 428 270 L560 270 L560 320 Z" fill="var(--band)"/>
    <path d="M0 314 L350 292 Q372 290 388 278 Q404 266 428 266 L560 266" fill="none" stroke="var(--brand-blue)" stroke-width="3"/>
  </svg>
  <div class="footer-web">ARDENTRIG.COM</div>
</section>

</body>
</html>
```